New Packaging Design for Olives

We are looking for a new packaging design for our product.
- Clear plastic cup container
- 90mm round lid and tapers down to 45mm base
- We do not want a box
- We would like a cardboard wrap around.
Product:
- Pitted Kalamata Olives
- 90g Net
We would like to product to be displayed from top view and side view.
We would like an image of kalamata olives on the packaging
our logo to appear on top and side
the bottom of the packaging to have room for a bar code, ingredients & nutritional panel.
This product is designed to target the accommodation/hotel market and we are wanting a classy looking design to attract mini bar customers.
Attached is an image of the cup & an internal mock up and our company logo.
We need a design that will seamlessly work across a variety of products including salsa, chilli sauce, tomato sauce and others.
Hotel Mini bar at 4 to 5 star hotels
Hotel

```html
<!DOCTYPE html>
<html lang="en">
<head>
<meta charset="utf-8">
<title>Hartwells Pitted Kalamata Olives – Lid and Wrap Labels</title>
<link rel="stylesheet" href="https://fonts.googleapis.com/css2?family=Didact+Gothic&family=Roboto:wght@700&display=swap">
<style>
  :root {
    --stage: #e4e4e6;
    --label-red: #d0232b;
    --label-black: #000000;
    --panel-black: #0e0405;
    --olive-band: #7c7620;
    --brand-yellow: #f2e51a;
    --copy-olive: #b0a342;
    --net-white: #ffffff;
    --olive-dark: #050507;
    --olive-light: #5a5a66;
  }
  html, body {
    margin: 0;
    padding: 0;
    overflow: hidden;
  }
  body {
    width: 1200px;
    height: 1200px;
    background: var(--stage);
    position: relative;
    font-family: "Didact Gothic", "Century Gothic", sans-serif;
  }
  .lid-label {
    position: absolute;
    left: 320px;
    top: 30px;
    width: 560px;
    height: 560px;
  }
  .wrap-label {
    position: absolute;
    left: 220px;
    top: 630px;
    width: 760px;
    height: 538px;
  }
  .brand-name {
    font-family: "Didact Gothic", "Century Gothic", sans-serif;
    fill: var(--brand-yellow);
  }
  .product-copy {
    font-family: "Didact Gothic", "Century Gothic", sans-serif;
    fill: var(--copy-olive);
  }
  .net-weight {
    font-family: "Roboto", Arial, sans-serif;
    font-weight: 700;
    fill: var(--net-white);
  }
  .band-black { fill: var(--label-black); }
  .band-red { fill: var(--label-red); }
  .band-olive { fill: var(--olive-band); }
  .title-panel { fill: var(--panel-black); }
  .brand-dot { fill: var(--label-red); }
</style>
</head>
<body>

  <!-- Round lid label -->
  <svg class="lid-label" viewBox="0 0 496 496" aria-label="Lid label">
    <defs>
      <clipPath id="lid-shape">
        <circle cx="248" cy="248" r="248"/>
      </clipPath>
      <radialGradient id="olive-tone-lid" cx="0.38" cy="0.35" r="0.7">
        <stop offset="0" stop-color="var(--olive-light)"/>
        <stop offset="1" stop-color="var(--olive-dark)"/>
      </radialGradient>
    </defs>
    <g clip-path="url(#lid-shape)">
      <rect class="band-black" x="0" y="0" width="496" height="28"/>
      <rect class="band-red" x="0" y="28" width="496" height="344"/>
      <rect class="band-olive" x="0" y="372" width="496" height="48"/>
      <rect class="band-black" x="0" y="420" width="496" height="76"/>

      <rect class="title-panel" x="23" y="110" width="397" height="190"/>
      <circle class="brand-dot" cx="300" cy="170" r="34"/>
      <text class="brand-name" x="40" y="206" font-size="62" textLength="345" lengthAdjust="spacingAndGlyphs">Hartwells</text>
      <text class="net-weight" x="336" y="250" font-size="17">90g NET</text>
      <text class="product-copy" x="40" y="253" font-size="25">Pitted</text>
      <text class="product-copy" x="40" y="286" font-size="25" textLength="272" lengthAdjust="spacingAndGlyphs">KALAMATA OLIVES</text>

      <ellipse role="img" aria-label="Illustration of a glossy black kalamata olive with olive leaves"
               cx="332" cy="356" rx="68" ry="58" fill="url(#olive-tone-lid)"/>
    </g>
  </svg>

  <!-- Wrap-around side label -->
  <svg class="wrap-label" viewBox="0 0 562 398" aria-label="Wrap-around label">
    <defs>
      <radialGradient id="olive-tone-wrap" cx="0.38" cy="0.35" r="0.7">
        <stop offset="0" stop-color="var(--olive-light)"/>
        <stop offset="1" stop-color="var(--olive-dark)"/>
      </radialGradient>
    </defs>
    <rect class="band-black" x="0" y="0" width="518" height="38"/>
    <rect class="band-black" x="0" y="38" width="40" height="308"/>
    <rect class="band-red" x="40" y="38" width="478" height="308"/>
    <rect class="band-olive" x="518" y="0" width="44" height="398"/>
    <rect class="band-olive" x="0" y="346" width="518" height="52"/>

    <rect class="title-panel" x="105" y="112" width="353" height="168"/>
    <circle class="brand-dot" cx="346" cy="168" r="32"/>
    <text class="brand-name" x="118" y="201" font-size="56" textLength="318" lengthAdjust="spacingAndGlyphs">Hartwells</text>
    <text class="net-weight" x="380" y="237" font-size="16">90g NET</text>
    <text class="product-copy" x="118" y="240" font-size="23">Pitted</text>
    <text class="product-copy" x="118" y="268" font-size="23" textLength="242" lengthAdjust="spacingAndGlyphs">KALAMATA OLIVES</text>

    <ellipse role="img" aria-label="Illustration of a glossy black kalamata olive with olive leaves"
             cx="372" cy="326" rx="55" ry="50" fill="url(#olive-tone-wrap)"/>
  </svg>

</body>
</html>
```